PLAV Brochure Design Project

I need a brochure for my new project management company.
the scope covers all engineering aspects of developments.
Green design is also included. so, I would like to see colours representing the industry and sustainability. soft colours really.
Hello, I'm attaching herewith the text, images, and the logo that i want to appear on the brochure
Target Market(s)
developers, investors, governments
Industry/Entity Type
Industry
Look and feel

```html
<!DOCTYPE html>
<html lang="en">
<head>
<meta charset="UTF-8">
<title>PLAV Project Management Brochure</title>
<link href="https://fonts.googleapis.com/css2?family=Marcellus+SC&family=Open+Sans:wght@400;600;700&display=swap" rel="stylesheet">
<style>
  :root {
    --blue: #3f7fc4;
    --blue-light: #8db7e3;
    --ink: #1a1a1a;
    --heading: #2b3440;
    --rule: #555;
    --grey: #6b7480;
    --paper: #ffffff;
  }
  * { margin: 0; padding: 0; box-sizing: border-box; }
  html, body { width: 1200px; height: 800px; overflow: hidden; background: var(--paper); }
  .brochure {
    position: relative; width: 1200px; height: 800px; overflow: hidden;
    font-family: "Open Sans", Arial, sans-serif; color: var(--ink);
  }
  .brand-block {
    position: absolute; left: 0; top: 0; width: 197px; height: 197px;
    background: linear-gradient(160deg, var(--blue-light), var(--blue));
  }
  .brand-square {
    position: absolute; left: 26px; top: 208px; width: 14px; height: 14px;
    background: var(--blue);
  }
  .brand-name {
    position: absolute; left: 48px; top: 192px; line-height: 1.1;
    font-family: "Open Sans", Arial, sans-serif; font-weight: 700;
    font-size: 44px; color: var(--blue); letter-spacing: 2px;
  }
  .brand-tagline {
    position: absolute; left: 26px; top: 250px;
    font-size: 14px; letter-spacing: 3px; color: var(--grey); font-weight: 600;
  }
  .tower-photo {
    position: absolute; left: 387px; top: 0; width: 214px; height: 298px;
    background: linear-gradient(180deg, #cfd9e4 0%, #aebdcc 60%, #7f9a6e 88%, #5d7456 100%);
  }
  .about-band {
    position: absolute; left: 0; top: 298px; width: 601px; height: 98px;
    background: linear-gradient(90deg, var(--blue) 0%, var(--blue-light) 40%, rgba(255,255,255,0) 100%);
  }
  .about-title {
    position: absolute; left: 95px; top: 302px;
    font-family: "Marcellus SC", Georgia, serif; font-size: 96px; line-height: 1;
    font-weight: 400; color: var(--heading); letter-spacing: 1px; white-space: nowrap;
  }
  .about-copy {
    position: absolute; left: 30px; top: 410px; width: 562px;
    font-size: 13px; line-height: 18.8px; font-weight: 600;
  }
  .about-copy p + p { margin-top: 18.8px; }
  .spine { position: absolute; left: 603px; top: 0; width: 1.5px; height: 800px; background: var(--rule); }
  .services-band {
    position: absolute; left: 604px; top: 60px; width: 596px; height: 74px;
    background: linear-gradient(90deg, rgba(255,255,255,0) 0%, var(--blue-light) 35%, var(--blue) 100%);
  }
  .services-title {
    position: absolute; left: 610px; top: 88px;
    font-family: "Marcellus SC", Georgia, serif; font-size: 28px; line-height: 1;
    font-weight: 400; color: var(--heading); white-space: nowrap;
  }
  .services-copy {
    position: absolute; left: 630px; top: 198px; width: 368px;
    font-size: 11.4px; line-height: 15.2px; font-weight: 600;
  }
  .services-copy p + p { margin-top: 15.2px; }
  .side-rule { position: absolute; left: 1004px; top: 188px; width: 1.5px; height: 590px; background: var(--rule); }
  .side-note {
    position: absolute; left: 1045px; top: 196px; width: 140px;
    font-size: 11.4px; line-height: 15.2px; font-weight: 600;
  }
</style>
</head>
<body>
<div class="brochure">
  <section class="about-panel">
    <div class="brand-block"></div>
    <div class="brand-square"></div>
    <div class="brand-name">PLAV</div>
    <div class="brand-tagline">PROJECT MANAGEMENT</div>
    <div class="tower-photo" role="img" aria-label="Photograph of modern glass towers with steel frames rising above palm trees"></div>
    <div class="about-band"></div>
    <h1 class="about-title">About Us</h1>
    <div class="about-copy">
      <p>Since its establishment in 2005, PLAV has offered the highest quality services to leading enterprises belonging to several different industrial sectors. Aimed at achieving excellence and exposing innovation in all of our services, we have built a profile that is filled with project completion accomplishments marked by the highest quality, and all these have been done within the allotted budgets and exactly as scheduled.</p>
      <p>We provide Working Agreements and Alliance services and have developed considerable experience, which has helped us in gaining proficiency and quality in all our work. Many different organizations including both consultants and contractors, with roots sprung throughout the country and across international borders as well, have availed our services and built lasting business relationships with us. We have successfully completed all our projects by combining our joint resources with third parties.</p>
      <p>Our skill sets comprise of both technical and project management abilities which we use for providing assistance to our clients. We help them in several different projects that range from developing completely new models, processes or methodologies to applying the current technologies for up-gradation of existing facilities.</p>
    </div>
  </section>

  <div class="spine"></div>

  <section class="services-panel">
    <div class="services-band"></div>
    <h2 class="services-title">OUR PROJECT MANAGEMENT SERVICES</h2>
    <div class="services-copy">
      <p>We exhibit professionalism and have expertise in project management. We know exactly what it takes to help a team move forward and execute the projects successfully through all stages no matter what obstacles sprout up in the way.</p>
      <p>In the initial phases, we develop a complete understanding of our clients' goals. Based on this, we draft out a plan, finalize the sites and determine a suitable budget for the project. In the design development phase, we manage the strategies, build an executable model and help our clients balance the objectives, project constraints and associated risks. We analyse all possible procurement options, integrate the designs with the outcomes while ensuring that they lie in the budget, and translate all that is involved into a complete execution plan. In the control and delivery phase, we make sure the plan will fulfil the business needs and that we have taken all measures to minimize risks. In the last phase of the project lifecycle, we ascertain that project has been executed as agreed and transfer the assets to the management.</p>
      <p>We are an independent advisor and can give you suggestions and recommendations in a timely manner, such that the required design, planning and commercial inputs make it possible to achieve the required outcomes. We ensure that all our clients are able to avail opportunities for development by helping them in determining the right market products and developing sound business cases. We can provide advice in any aspect, be it impact analysis, development strategies, layout mix and specification, marketing and implementation.</p>
      <p>The way in which we organise our projects help us to maintain a sharper focus, increase the efficiency and deliver the outcomes in an effective manner. It also lets us in implementing better risk management strategies.</p>
      <p>We have relationships with global enterprises, public sector companiesand commercial occupiers and have helped them in executing multi level projects.</p>
    </div>
    <div class="side-rule"></div>
    <p class="side-note">More info About your Company in its project management services goes here</p>
  </section>
</div>
</body>
</html>
```